Web Design Project

I'm looking for a major redesign for my existing photographic art website: www.brightmeadowframes.com. Here are my complaints about the current layout: 1) It looks unsophisticated (we will, of course, delete the "sale" banner; 2) the images are vastly too small when displayed in the gallery; 3) I'm not wild about the navigation; 4) the Flash has got to go; 4) there has to be an easy way to significantly enlarge the photos for viewing; 5) the copy is a bit over the top - we will be rewriting it. Other than that, it's a good site :)

The market for the photography is principally commercial applications - interior designers, etc. who are concerned with how these images will look in hospitals, office buildings, etc. The leading competitor in this space has a much better site: www.walterpikens.com. Another site worth viewing is: www.morvelt.com. This site is much more akin to my site.

We will be reducing the number of photos available. Total count will be approximately 400. The largest collection will be the "digital garden" - close up photography of flowers, plants, etc.
Updates

I am amazed at the quality of the submissions - which has made the selection process very, very difficult. Each of you should be very proud of the quality of work you produce. Beyond this web-site, which is a "sideline" for me, I run a large marketing organization....and have shared these submissions with all of my colleagues who were duly impressed. Hopefully we will have an opportunity to work with you on a differentp project!

Thank you!!!
Peter

Industry/Entity Type

Digital

```html
<!DOCTYPE html>
<html lang="en">
<head>
<meta charset="utf-8">
<title>Photography by Peter Quillane</title>
<link href="https://fonts.googleapis.com/css2?family=Source+Sans+3:wght@400;600;700&display=swap" rel="stylesheet">
<style>
:root{
  --red:#c70000;
  --red-dark:#9e0000;
  --red-light:#e41010;
  --ink:#333333;
  --black:#111111;
  --grey-text:#666666;
  --panel:#e3e2e0;
  --texture:#c9c9c9;
  --white:#ffffff;
}
*{box-sizing:border-box;margin:0;padding:0}
html,body{width:1200px;height:908px;overflow:hidden}
body{
  position:relative;
  font-family:"Source Sans 3",Arial,sans-serif;
  color:var(--ink);
  background:var(--white);
}
.site-header{
  position:absolute;left:0;top:0;width:1200px;height:101px;
  background:linear-gradient(#ffffff,#ebebeb);
}
.brand{
  position:absolute;left:120px;top:0;width:160px;height:100px;
  display:flex;align-items:center;justify-content:center;
}
.brand-name{font-size:19px;font-weight:600;color:var(--red)}
.tagline{position:absolute;left:293px;top:29px;font-size:20px;line-height:25px;color:#4a4a4a}
.tagline strong{color:var(--red);font-weight:700}
.account{position:absolute;right:120px;top:17px;display:flex;gap:7px}
.account a{
  background:#555;color:#fff;font-size:12px;text-decoration:none;
  padding:1px 7px;border-radius:2px;line-height:16px;
}
.cart{position:absolute;right:122px;top:62px;display:flex;align-items:center;gap:6px;font-size:12px}
.cart-count{color:var(--red)}
.cart a{color:#555;font-size:13px;text-decoration:underline}
.main-nav{
  position:absolute;left:0;top:101px;width:1200px;height:39px;
  background:linear-gradient(var(--red-light),var(--red-dark));
  box-shadow:0 2px 3px rgba(0,0,0,.35);
}
.main-nav ul{position:absolute;left:120px;top:0;display:flex;list-style:none;height:39px}
.main-nav li{
  height:39px;line-height:38px;color:#fff;font-size:15px;text-align:center;
  border-right:1px solid rgba(255,255,255,.18);
}
.main-nav li.active{background:linear-gradient(#2a2a2a,#000);width:91px}
.main-nav li.nav-architects{width:179px}
.main-nav li.nav-about{width:145px}
.main-nav li.nav-ordering{width:177px}
.main-nav li.nav-contact{width:108px;border-right:0}
.search{
  position:absolute;left:835px;top:9px;width:245px;height:22px;background:#fff;
  border-radius:2px;font-size:13px;font-style:italic;color:#888;padding:2px 7px;
}
.search svg{position:absolute;right:7px;top:4px}
.stage{
  position:absolute;left:0;top:140px;width:1200px;height:300px;
  background:linear-gradient(var(--texture),#e3e3e3 60%,#ffffff);
}
.promo{position:absolute;left:0;width:1200px;text-align:center;font-weight:700}
.promo-title{top:154px;font-size:27px;color:var(--red);text-shadow:0 0 2px #fff}
.promo-note{top:187px;font-size:24px;color:var(--black);text-shadow:0 0 2px #fff}
.slide-frame{
  position:absolute;left:209px;top:235px;width:783px;height:386px;background:#fff;padding:6px;
}
.slide-photo{
  width:771px;height:374px;
  background:linear-gradient(#c28a2c 0%,#e9a63e 22%,#b07a3a 30%,#5b5048 40%,#3b3a39 70%,#1d1b1a 100%);
}
.slide-shadow{
  position:absolute;left:235px;top:618px;width:740px;height:26px;
  background:radial-gradient(ellipse at 50% 0,rgba(0,0,0,.55),rgba(0,0,0,0) 70%);
}
.slide-arrow{position:absolute;top:393px}
.slide-arrow.prev{left:125px}
.slide-arrow.next{left:1003px}
.intro{position:absolute;left:123px;top:679px;width:915px;font-size:15px;line-height:20px;color:#3a3a3a}
.site-footer{
  position:absolute;left:120px;top:793px;width:960px;height:72px;background:var(--panel);border-radius:8px;
}
.footer-phone{position:absolute;left:20px;top:27px;font-size:15px;font-weight:700;color:var(--black)}
.footer-nav{position:absolute;right:11px;top:11px;font-size:12.5px;color:var(--black)}
.footer-nav span.sep{margin:0 13px}
.copyright{position:absolute;right:11px;top:45px;font-size:12.5px;color:var(--grey-text)}
</style>
</head>
<body>
<header class="site-header">
  <div class="brand"><span class="brand-name">Bright Meadow</span></div>
  <p class="tagline">Photography by <strong>Peter Quillane</strong><br>Photography that transcends our normal view of the world</p>
  <nav class="account"><a href="#">Login</a><a href="#">Sign Up</a></nav>
  <div class="cart">
    <span class="cart-count">You have 0 item(s) in your cart.</span>
    <svg width="20" height="16" viewBox="0 0 20 16" aria-hidden="true"><path d="M1 2h3l2 8h10l2-6H5" fill="none" stroke="#444" stroke-width="1.6"/><circle cx="8" cy="13.5" r="1.5" fill="#444"/><circle cx="15" cy="13.5" r="1.5" fill="#444"/></svg>
    <a href="#">Lightbox</a>
  </div>
</header>
<nav class="main-nav">
  <ul>
    <li class="active">Gallery</li>
    <li class="nav-architects">Architects/Designers</li>
    <li class="nav-about">About the artist</li>
    <li class="nav-ordering">Ordering infomation</li>
    <li class="nav-contact">Contact Us</li>
  </ul>
  <div class="search">Search...
    <svg width="14" height="14" viewBox="0 0 14 14" aria-hidden="true"><circle cx="5.5" cy="5.5" r="4" fill="none" stroke="#333" stroke-width="2"/><path d="M8.5 8.5l4 4" stroke="#333" stroke-width="2.4"/></svg>
  </div>
</nav>
<div class="stage"></div>
<p class="promo promo-title">SALE! ALL PHOTOGRAPHS 30% OFF.</p>
<p class="promo promo-note">Discount will be applied automatically in the shopping cart as part of the ordering process.</p>
<div class="slide-shadow"></div>
<div class="slide-frame"><div class="slide-photo" role="img" aria-label="Seascape photograph: golden sunset sky over the ocean with dark rocks in the foreground"></div></div>
<svg class="slide-arrow prev" width="72" height="72" viewBox="0 0 72 72" aria-label="Previous"><defs><linearGradient id="arrowFill" x1="0" y1="0" x2="0" y2="1"><stop offset="0" stop-color="#ffffff"/><stop offset="1" stop-color="#c8c8c8"/></linearGradient></defs><circle cx="36" cy="36" r="34" fill="url(#arrowFill)" stroke="#a5a5a5" stroke-width="2"/><circle cx="36" cy="36" r="27" fill="none" stroke="#d0d0d0" stroke-width="1.5"/><path d="M42 22L28 36l14 14" fill="none" stroke="#888" stroke-width="8" stroke-linecap="round" stroke-linejoin="round"/></svg>
<svg class="slide-arrow next" width="72" height="72" viewBox="0 0 72 72" aria-label="Next"><circle cx="36" cy="36" r="34" fill="url(#arrowFill)" stroke="#a5a5a5" stroke-width="2"/><circle cx="36" cy="36" r="27" fill="none" stroke="#d0d0d0" stroke-width="1.5"/><path d="M30 22l14 14-14 14" fill="none" stroke="#888" stroke-width="8" stroke-linecap="round" stroke-linejoin="round"/></svg>
<p class="intro">Welcome to the world of Peter Quillane. Come in and enjoy a place where stunning horizons meet glorious skies. A place where light and shade dance together in flawless rhythm. Come in and discover a world of photography that begins and ends with a shutter. Come in, relax and browse the gallery. You are about to experience some of the most inspiring and enchanting imagery the world has to offer.</p>
<footer class="site-footer">
  <p class="footer-phone">Phone: 877-555-0142</p>
  <p class="footer-nav">Gallery<span class="sep">|</span>Architects/Designers<span class="sep">|</span>About the Artist<span class="sep">|</span>Ordering Information<span class="sep">|</span>Contact Us</p>
  <p class="copyright">© 2010 Quillane Photography</p>
</footer>
</body>
</html>
```